Word Page Templates x 5

1 x Letterhead Template with Header and Footer able to be printed to paper and pdf with non blurry resolution
- File attached looks ok on computer screen but does not print the same
- We are wanting it to print like it looks on the screen
- We are wanting it to print not fuzzy in resolution
- We are wanting the banner to be on the absolute edge of the page like it is on the computer screen
- We are needing to print this to paper and pdf with perfect resolution and colour

Please can someone help us!!

I have provided the logo files in our posession. If better resolutions are required please let us know.

We are also wanting 4 simple page templates to be setup in Landscape and Portrait orientation as well once we are happy with the letterhead that is provided samples have been provided
Updates

Hi all I have the vector files available now along with a Colour profile

Requirements
Must have
• Clear when printed on A4 Paper
Should not have
• Blurry images, Colour must be correct (same as Logo) - Please reference our website if need be ..... vornal.com.au

```html
<!DOCTYPE html>
<html lang="en">
<head>
<meta charset="utf-8">
<title>Vornal Stationery Templates</title>
<link rel="stylesheet" href="https://fonts.googleapis.com/css2?family=Open+Sans:wght@400;600&display=swap">
<style>
  :root{
    --green:#3aa935;
    --blue:#1f5fa8;
    --navy:#173a6b;
    --text:#5b5f66;
    --rule:#c9ced6;
    --badge:#dfe5ec;
    --backdrop:#d7d8da;
    --paper:#ffffff;
  }
  *{box-sizing:border-box;margin:0;padding:0}
  html,body{width:800px;height:1200px;overflow:hidden}
  body{background:var(--backdrop);font-family:"Open Sans",Arial,sans-serif;position:relative}

  .sheet{position:absolute;background:var(--paper);overflow:hidden;box-shadow:0 1px 4px rgba(0,0,0,.18)}
  .sheet--letterhead{left:200px;top:24px;width:400px;height:566px;font-size:10px}
  .sheet--portrait{width:212px;height:300px;top:620px;font-size:5.3px}
  .sheet--landscape{width:311px;height:220px;top:950px;font-size:5.3px}
  .pos-1{left:38px}.pos-2{left:294px}.pos-3{left:550px}
  .pos-4{left:60px}.pos-5{left:429px}

  .band{position:absolute;left:0;right:0;height:.45em;background:linear-gradient(90deg,var(--green),var(--blue) 60%,var(--navy))}
  .band--top{top:0}
  .band--bottom{bottom:0}

  .brand{position:absolute;left:2.8em;top:2.4em;font-weight:600;font-size:1.9em;line-height:1;color:var(--blue);white-space:nowrap}
  .brand--foot{top:auto;left:auto;right:2.8em;bottom:1.6em;font-size:1.3em}

  .contact{position:absolute;right:2.8em;top:2.2em;font-size:.52em;line-height:1.75;color:var(--text);list-style:none;white-space:nowrap}
  .contact li{display:flex;align-items:center;gap:.6em}
  .contact svg{width:1em;height:1em;fill:var(--green);flex:none}

  .letter{position:absolute;left:2.8em;right:2.8em;top:8.6em;color:var(--text)}
  .letter__title{font-size:1.15em;font-weight:600;color:var(--blue);margin-bottom:.9em}
  .letter p{font-size:.6em;line-height:1.65;margin-bottom:1.2em}
  .letter__sign{margin-top:2em}

  .footer{position:absolute;left:2.8em;right:2.8em;bottom:1.6em;border-top:.1em solid var(--rule);padding-top:.6em}
  .footer__note{font-size:.45em;color:var(--navy);font-weight:600;margin-bottom:.6em;white-space:nowrap}
  .footer__badges{display:flex;gap:.8em;align-items:center}
  .badge{width:4.2em;height:1.8em;background:var(--badge);border-radius:.2em}
  .badge--round{width:1.8em;border-radius:50%}
  .footer .brand--foot{right:0;bottom:0}
</style>
</head>
<body>

<section class="sheet sheet--letterhead">
  <div class="band band--top"></div>
  <div class="brand">VORNAL</div>
  <ul class="contact">
    <li><svg viewBox="0 0 10 10"><path d="M5 0a3.5 3.5 0 0 0-3.5 3.5C1.5 6 5 10 5 10s3.5-4 3.5-6.5A3.5 3.5 0 0 0 5 0zm0 5a1.5 1.5 0 1 1 0-3 1.5 1.5 0 0 1 0 3z"/></svg>14 Harbour Road, Portside QLD 4000</li>
    <li><svg viewBox="0 0 10 10"><path d="M2 0l2 2.5-1.2 1.2a6 6 0 0 0 3.5 3.5L7.5 6 10 8l-1.5 2C4 10 0 6 0 1.5z"/></svg>07 5550 1234</li>
    <li><svg viewBox="0 0 10 10"><path d="M0 2h10v6H0z"/></svg>info@vornal.com.au</li>
    <li><svg viewBox="0 0 10 10"><circle cx="5" cy="5" r="5"/></svg>vornal.com.au</li>
  </ul>

  <article class="letter">
    <h1 class="letter__title">Business Proposals</h1>
    <p>Vornal provides practical engineering support for industrial clients across the region. Our team plans, builds and maintains plant equipment with a strong focus on safety, quality and clear communication. We work closely with every client to understand the site, the schedule and the budget before work begins.</p>
    <p>This proposal outlines the scope of works, the proposed timeline and the resources we will allocate to the project. Each stage includes a review point so that changes can be agreed early and costs remain predictable. Our supervisors report progress weekly and keep detailed records of inspections, materials and labour hours for your files.</p>
    <p>We look forward to working with you and are happy to answer any questions about this proposal. Please contact our office to arrange a site visit or a meeting at a time that suits you.</p>
    <p class="letter__sign">Kind regards,<br><br>Operations Manager</p>
  </article>

  <footer class="footer">
    <div class="footer__note">Proud members of industry associations</div>
    <div class="footer__badges">
      <span class="badge"></span><span class="badge badge--round"></span><span class="badge"></span>
    </div>
    <div class="brand brand--foot">VORNAL</div>
  </footer>
  <div class="band band--bottom"></div>
</section>

<section class="sheet sheet--portrait pos-1">
  <div class="band band--top"></div>
  <div class="brand">VORNAL</div>
  <ul class="contact">
    <li>14 Harbour Road, Portside QLD 4000</li><li>07 5550 1234</li><li>info@vornal.com.au</li><li>vornal.com.au</li>
  </ul>
  <footer class="footer">
    <div class="footer__note">Proud members of industry associations</div>
    <div class="footer__badges">
      <span class="badge"></span><span class="badge badge--round"></span><span class="badge"></span>
    </div>
    <div class="brand brand--foot">VORNAL</div>
  </footer>
  <div class="band band--bottom"></div>
</section>

<section class="sheet sheet--portrait pos-2">
  <div class="band band--top"></div>
  <div class="brand">VORNAL</div>
  <ul class="contact">
    <li>14 Harbour Road, Portside QLD 4000</li><li>07 5550 1234</li><li>info@vornal.com.au</li><li>vornal.com.au</li>
  </ul>
  <div class="brand brand--foot">VORNAL</div>
  <div class="band band--bottom"></div>
</section>

<section class="sheet sheet--portrait pos-3">
  <div class="band band--top"></div>
  <div class="brand">VORNAL</div>
  <ul class="contact">
    <li>14 Harbour Road, Portside QLD 4000</li><li>07 5550 1234</li><li>info@vornal.com.au</li><li>vornal.com.au</li>
  </ul>
  <div class="band band--bottom"></div>
</section>

<section class="sheet sheet--landscape pos-4">
  <div class="band band--top"></div>
  <div class="brand brand--foot">VORNAL</div>
  <div class="band band--bottom"></div>
</section>

<section class="sheet sheet--landscape pos-5">
  <div class="band band--top"></div>
  <div class="brand">VORNAL</div>
  <ul class="contact">
    <li>14 Harbour Road, Portside QLD 4000</li><li>07 5550 1234</li><li>info@vornal.com.au</li><li>vornal.com.au</li>
  </ul>
  <div class="band band--bottom"></div>
</section>

</body>
</html>
```